Dentistry Office

We want a new design for a Dentist's office website.

The theme is: "We provide high quality, state-of-the-art, dental care in a comfortable, caring environment."

The site currently has a menu on the left of the page with about 40 items on it. There is a great deal of textual content on each page, plus several illustrations.

We want to do this using CSS, so we need specifications in the CSS for all possible elements. The CSS needs to be named in a logical manner for easy use.

Every dentist on the planet seems to use lots of Flash. We don't want to because it is so distracting. We are looking for an elegant solution targeting 24-55 age group, but not excluding anyone.

The following (from another dentist's site) can give you a taste of what we want to communicate on the site:

"After 20 years of teaching dentists how to refine their technique and many years of writing textbooks, I currently devote my time to my office and the hands-on practice of dentistry. I'd like to welcome you personally to my dental practice, and I invite you to meet my highly experienced team of professionals.

"We have offered complete dental care of the highest quality since 1978. We provide Preventive Services, Tooth Whitening and Cosmetic Dentistry for a beautiful smile, Endodontics (root canal treatment) to treat painful teeth, Sedation Dentistry so you can relax, and Dental Implants to restore what is missing. We offer total care.

"Our approach to your health is simple: We use our education, experience and dedication to provide every patient with superior dental care.

"This passion for excellence is not just a goal, but a standard every member of our team holds.

"We also pride ourselves with our state of the art procedures, training and technology. This includes creating a beautiful smile using techniques that preserve as much of the original tooth as possible.

"Our abilities are renowned throughout the dental profession and I hope if you have any questions you will contact us by an e-mail note, by phone or just by dropping by."

Keep in mind the screen shape and dimensions. Your design needs to work in the normal screen proportions, regardless of how it looks when you post it here. Scrolling is OK, but the first impression needs to work.

Keep in mind that there will be about 250 words, or more, on each page.

Competitors web sites:

http://www.brevalkoortho.example/

http://www.quimbelfieldcare.example/

http://www.grinsatdoverellclinic.example/

http://www.trunwickfamilydentalcare.example/

http://www.morvanhaledental.example/

http://www.ubrigandental.example/

We need to compete with these.

Target Market(s)

Generally adults seeking the most experienced and comfortable-to-be-with dentist.

Industry/Entity Type

Training

Requirements
Must have
• Must stand apart from other dentists.
• Must be elegant.
• Must have a horizontal menu structure across all columns, NOT a vertical that requires scrolling, no popout, pop down, etc. menus.
• We are looking for something special.
• Do not waste your time or ours putting up templates and things you have used before.
• Personally, I do not see how someone outside the US can understand the northern California dental market. But you are welcome to try.
Should not have
• Flash or graphics that move
• The look of a template
• Folksy fonts
• Looks like you used it 20 times before

```html
<!DOCTYPE html>
<html lang="en">
<head>
<meta charset="utf-8">
<title>Dental Care</title>
<link href="https://fonts.googleapis.com/css2?family=Marcellus&family=Parisienne&family=Source+Sans+3:wght@400;600&family=Open+Sans:wght@700&display=swap" rel="stylesheet">
<style>
:root{
  --slate:#2c3a45;
  --slate-top:#3e4d58;
  --red:#c80606;
  --red-dark:#a90000;
  --blue:#0a5eb3;
  --blue-line:#3d82c8;
  --heading-blue:#1a66b8;
  --ink:#111;
  --muted:#999;
  --gold:#f4c20d;
  --white:#fff;
}
*{margin:0;padding:0;box-sizing:border-box}
html,body{width:1005px;height:1200px;overflow:hidden;background:var(--white)}
body{position:relative;font-family:Arial,Helvetica,sans-serif;color:var(--ink)}

.site-header{position:absolute;left:0;top:0;width:1005px;height:292px;
  background:linear-gradient(180deg,#4f5f6b 0%,var(--slate) 18%,var(--slate) 100%);overflow:hidden}
.brand{position:absolute;left:46px;top:58px;color:var(--white)}
.brand-name{font-family:"Marcellus",serif;font-size:44px;line-height:48px}
.brand-tag{font-family:"Open Sans",sans-serif;font-weight:700;font-size:11px;color:var(--gold);margin-top:2px}
.header-slogan{position:absolute;left:32px;top:156px;width:310px;font-family:"Parisienne",cursive;
  font-size:22px;line-height:29px;color:var(--white)}

.photo-frame{position:absolute;background:var(--white);padding:7px}
.photo-frame .photo{width:100%;height:100%}
.frame-left{left:342px;top:92px;width:150px;height:230px;transform:rotate(-9deg)}
.frame-left .photo{background:linear-gradient(135deg,#e9ecef,#c7b8ae 60%,#6f6660)}
.frame-right{left:830px;top:86px;width:140px;height:240px;transform:rotate(8deg)}
.frame-right .photo{background:linear-gradient(135deg,#f2f3f4,#dad5d0 60%,#c9a88f)}
.frame-main{left:458px;top:33px;width:400px;height:275px}
.frame-main .photo{background:linear-gradient(120deg,#d6dde2,#e8e2d8 45%,#b7c9dd 70%,#b78b57)}

.main-nav{position:absolute;left:0;top:291px;width:1005px;height:43px;background:var(--red);
  border-bottom:3px dotted var(--white)}
.main-nav ul{list-style:none;display:flex;align-items:center;height:40px;padding-left:20px}
.main-nav li{font-family:"Source Sans 3",sans-serif;font-size:17px;color:var(--white);white-space:nowrap}
.main-nav .sep{margin:0 13px}

.side-menu{position:absolute;left:15px;top:352px;width:226px;height:714px;border-radius:7px;
  background:var(--blue);overflow:hidden}
.side-menu-title{height:36px;background:linear-gradient(180deg,#e01212,var(--red-dark));
  border-bottom:2px dotted var(--white);color:var(--white);font-family:"Source Sans 3",sans-serif;
  font-size:16px;padding:6px 0 0 23px}
.side-menu ul{list-style:none;margin-top:17px}
.side-menu li{height:30px;border-bottom:1px dashed var(--blue-line);color:var(--white);font-size:12px;
  display:flex;align-items:center;padding-left:18px}
.side-menu li svg{margin-right:9px}

.welcome-title{position:absolute;left:279px;top:362px;font-family:"Marcellus",serif;font-size:29px;color:var(--ink)}
.welcome-title span{font-size:37px;color:var(--heading-blue)}
.title-rule{position:absolute;left:276px;top:410px;width:707px;border-top:1px dashed var(--muted)}

.intro-photo{position:absolute;left:669px;top:429px;width:314px;height:209px;padding:8px;
  background:var(--white);border:1px solid #cfe0ea;box-shadow:0 0 4px #9cc2da}
.intro-photo .photo{width:100%;height:100%;background:linear-gradient(120deg,#e3e9ec,#b9c3c9 50%,#5e4a3d)}

.article{position:absolute;left:283px;top:437px;width:692px;font-size:12px;line-height:18px}
.article p{margin-bottom:18px}
.article .narrow{width:370px}

.feature{position:absolute;top:898px;width:216px}
.feature h2{font-family:"Marcellus",serif;font-weight:400;font-size:20px;color:var(--heading-blue);
  margin-left:3px;height:40px}
.feature-card{width:216px;height:127px;border:1px solid #c8c8c8;border-radius:6px;padding:5px;
  box-shadow:0 1px 3px #ccc;background:var(--white)}
.feature-card .photo{position:relative;width:100%;height:100%;border-radius:3px;overflow:hidden}
.feature-label{position:absolute;left:0;right:0;bottom:6px;text-align:center;
  font-family:"Marcellus",serif;color:#111;text-shadow:0 0 3px #fff,0 0 3px #fff;display:flex;
  justify-content:center;align-items:center;gap:6px}
.call .photo{background:linear-gradient(120deg,#d9e2e8,#c9b9a8 55%,#6b4b3a)}
.implants .photo{background:linear-gradient(120deg,#e9e6e2,#d7c3b4 55%,#c9b4a4)}
.dentists .photo{background:linear-gradient(120deg,#eef0f2,#d6c7b2 45%,#e4e8ec)}

.site-footer{position:absolute;left:0;top:1100px;width:1005px;height:100px;background:var(--slate);
  border-top:3px dotted #cfd4d8}
.site-footer p{position:absolute;right:25px;top:39px;font-size:11px;color:var(--white);white-space:nowrap}
.site-footer .sep{margin:0 7px}
</style>
</head>
<body>

<header class="site-header">
  <div class="brand">
    <div class="brand-name">Dental Care</div>
    <div class="brand-tag">The Best Dental Care of Northern California</div>
  </div>
  <p class="header-slogan">We provide high quality, state-of-the-art, dental care in a comfortable, caring environment..</p>
  <div class="photo-frame frame-left"><div class="photo" role="img" aria-label="Dental assistant in mask treating a patient"></div></div>
  <div class="photo-frame frame-right"><div class="photo" role="img" aria-label="Relaxed patient in a dental chair"></div></div>
  <div class="photo-frame frame-main"><div class="photo" role="img" aria-label="Smiling hygienist showing dental floss to a patient"></div></div>
</header>

<nav class="main-nav">
  <ul>
    <li>Home</li><li class="sep">|</li>
    <li>About Us</li><li class="sep">|</li>
    <li>Our Practice</li><li class="sep">|</li>
    <li>Procedures</li><li class="sep">|</li>
    <li>Our Mission</li><li class="sep">|</li>
    <li>Dental Implants</li><li class="sep">|</li>
    <li>FAQs</li><li class="sep">|</li>
    <li>Smile Gallery</li><li class="sep">|</li>
    <li>Contact US</li>
  </ul>
</nav>

<aside class="side-menu">
  <div class="side-menu-title">Left Menu</div>
  <ul>
    <li><svg width="10" height="10" viewBox="0 0 10 10"><path d="M2 1l4 4-4 4M6 1l3 4-3 4" fill="none" stroke="#0a1f40" stroke-width="1.5"/></svg>Lorem Ipsum Dolor Sit Amet</li>
    <li><svg width="10" height="10" viewBox="0 0 10 10"><path d="M2 1l4 4-4 4M6 1l3 4-3 4" fill="none" stroke="#0a1f40" stroke-width="1.5"/></svg>Lorem Ipsum Dolor Sit Amet</li>
    <li><svg width="10" height="10" viewBox="0 0 10 10"><path d="M2 1l4 4-4 4M6 1l3 4-3 4" fill="none" stroke="#0a1f40" stroke-width="1.5"/></svg>Lorem Ipsum Dolor Sit Amet</li>
    <li><svg width="10" height="10" viewBox="0 0 10 10"><path d="M2 1l4 4-4 4M6 1l3 4-3 4" fill="none" stroke="#0a1f40" stroke-width="1.5"/></svg>Lorem Ipsum Dolor Sit Amet</li>
    <li><svg width="10" height="10" viewBox="0 0 10 10"><path d="M2 1l4 4-4 4M6 1l3 4-3 4" fill="none" stroke="#0a1f40" stroke-width="1.5"/></svg>Lorem Ipsum Dolor Sit Amet</li>
    <li><svg width="10" height="10" viewBox="0 0 10 10"><path d="M2 1l4 4-4 4M6 1l3 4-3 4" fill="none" stroke="#0a1f40" stroke-width="1.5"/></svg>Lorem Ipsum Dolor Sit Amet</li>
    <li><svg width="10" height="10" viewBox="0 0 10 10"><path d="M2 1l4 4-4 4M6 1l3 4-3 4" fill="none" stroke="#0a1f40" stroke-width="1.5"/></svg>Lorem Ipsum Dolor Sit Amet</li>
    <li><svg width="10" height="10" viewBox="0 0 10 10"><path d="M2 1l4 4-4 4M6 1l3 4-3 4" fill="none" stroke="#0a1f40" stroke-width="1.5"/></svg>Lorem Ipsum Dolor Sit Amet</li>
    <li><svg width="10" height="10" viewBox="0 0 10 10"><path d="M2 1l4 4-4 4M6 1l3 4-3 4" fill="none" stroke="#0a1f40" stroke-width="1.5"/></svg>Lorem Ipsum Dolor Sit Amet</li>
    <li><svg width="10" height="10" viewBox="0 0 10 10"><path d="M2 1l4 4-4 4M6 1l3 4-3 4" fill="none" stroke="#0a1f40" stroke-width="1.5"/></svg>Lorem Ipsum Dolor Sit Amet</li>
    <li><svg width="10" height="10" viewBox="0 0 10 10"><path d="M2 1l4 4-4 4M6 1l3 4-3 4" fill="none" stroke="#0a1f40" stroke-width="1.5"/></svg>Lorem Ipsum Dolor Sit Amet</li>
    <li><svg width="10" height="10" viewBox="0 0 10 10"><path d="M2 1l4 4-4 4M6 1l3 4-3 4" fill="none" stroke="#0a1f40" stroke-width="1.5"/></svg>Lorem Ipsum Dolor Sit Amet</li>
    <li><svg width="10" height="10" viewBox="0 0 10 10"><path d="M2 1l4 4-4 4M6 1l3 4-3 4" fill="none" stroke="#0a1f40" stroke-width="1.5"/></svg>Lorem Ipsum Dolor Sit Amet</li>
    <li><svg width="10" height="10" viewBox="0 0 10 10"><path d="M2 1l4 4-4 4M6 1l3 4-3 4" fill="none" stroke="#0a1f40" stroke-width="1.5"/></svg>Lorem Ipsum Dolor Sit Amet</li>
    <li><svg width="10" height="10" viewBox="0 0 10 10"><path d="M2 1l4 4-4 4M6 1l3 4-3 4" fill="none" stroke="#0a1f40" stroke-width="1.5"/></svg>Lorem Ipsum Dolor Sit Amet</li>
    <li><svg width="10" height="10" viewBox="0 0 10 10"><path d="M2 1l4 4-4 4M6 1l3 4-3 4" fill="none" stroke="#0a1f40" stroke-width="1.5"/></svg>Lorem Ipsum Dolor Sit Amet</li>
    <li><svg width="10" height="10" viewBox="0 0 10 10"><path d="M2 1l4 4-4 4M6 1l3 4-3 4" fill="none" stroke="#0a1f40" stroke-width="1.5"/></svg>Lorem Ipsum Dolor Sit Amet</li>
    <li><svg width="10" height="10" viewBox="0 0 10 10"><path d="M2 1l4 4-4 4M6 1l3 4-3 4" fill="none" stroke="#0a1f40" stroke-width="1.5"/></svg>Lorem Ipsum Dolor Sit Amet</li>
    <li><svg width="10" height="10" viewBox="0 0 10 10"><path d="M2 1l4 4-4 4M6 1l3 4-3 4" fill="none" stroke="#0a1f40" stroke-width="1.5"/></svg>Lorem Ipsum Dolor Sit Amet</li>
    <li><svg width="10" height="10" viewBox="0 0 10 10"><path d="M2 1l4 4-4 4M6 1l3 4-3 4" fill="none" stroke="#0a1f40" stroke-width="1.5"/></svg>Lorem Ipsum Dolor Sit Amet</li>
    <li><svg width="10" height="10" viewBox="0 0 10 10"><path d="M2 1l4 4-4 4M6 1l3 4-3 4" fill="none" stroke="#0a1f40" stroke-width="1.5"/></svg>Lorem Ipsum Dolor Sit Amet</li>
    <li><svg width="10" height="10" viewBox="0 0 10 10"><path d="M2 1l4 4-4 4M6 1l3 4-3 4" fill="none" stroke="#0a1f40" stroke-width="1.5"/></svg>Lorem Ipsum Dolor Sit Amet</li>
  </ul>
</aside>

<h1 class="welcome-title">welcome to <span>Dental Care</span></h1>
<div class="title-rule"></div>

<div class="intro-photo"><div class="photo" role="img" aria-label="Dentist showing a tooth model to a patient in the chair"></div></div>

<main class="article">
  <p class="narrow">"After 20 years of teaching dentists how to refine their technique and many years of writing textbooks, I currently devote my time to my office and the hands-on practice of dentistry. I'd like to welcome you personally to my dental practice, and I invite you to meet my highly experienced team of professionals.</p>
  <p class="narrow">"We have offered complete dental care of the highest quality since 1978. We provide Preventive Services, Tooth Whitening and Cosmetic Dentistry for a beautiful smile, Endodontics (root canal treatment) to treat painful teeth, Sedation Dentistry so you can relax, and Dental Implants to restore what is missing. We offer total care.</p>
  <p>"Our approach to your health is simple: We use our education, experience and dedication to provide every patient with superior dental care.</p>
  <p>"This passion for excellence is not just a goal, but a standard every member of our team holds.</p>
  <p>"We also pride ourselves with our state of the art procedures, training and technology. This includes creating a beautiful smile using techniques that preserve as much of the original tooth as possible.</p>
  <p>"Our abilities are renowned throughout the dental profession and I hope if you have any questions you will contact us by an e-mail note, by phone or just by dropping by."</p>
</main>

<section class="feature call" style="left:283px">
  <h2>Call Us</h2>
  <div class="feature-card"><div class="photo" role="img" aria-label="Woman talking on a phone">
    <div class="feature-label" style="font-size:30px;bottom:4px">555.245.1234</div>
  </div></div>
</section>

<section class="feature implants" style="left:525px">
  <h2>Dental Implants</h2>
  <div class="feature-card"><div class="photo" role="img" aria-label="Dentist holding a denture model beside a patient">
    <div class="feature-label" style="font-size:20px">More Information
      <svg width="24" height="24" viewBox="0 0 24 24"><circle cx="12" cy="12" r="11" fill="#111"/><path d="M6 12h11M13 8l4 4-4 4" fill="none" stroke="#fff" stroke-width="2"/></svg>
    </div>
  </div></div>
</section>

<section class="feature dentists" style="left:767px">
  <h2>Meet The Dentists</h2>
  <div class="feature-card"><div class="photo" role="img" aria-label="Two smiling dentists in white coats">
    <div class="feature-label" style="font-size:20px">View List of Dentists</div>
  </div></div>
</section>

<footer class="site-footer">
  <p>© Copyright Dental Care<span class="sep">|</span>All Rigghts&nbsp; Reserved&nbsp; Home<span class="sep">|</span>About Us<span class="sep">|</span>Our Practice<span class="sep">|</span>Procedures<span class="sep">|</span>Our Mission<span class="sep">|</span>Dental Implants<span class="sep">|</span>FAQs<span class="sep">|</span>Smile Gallery<span class="sep">|</span>Contact Us</p>
</footer>

</body>
</html>
```